Delivery Performance Dashboard for Web Portal

We need you to design a dashboard for our web portal. We deliver sand and stone to construction jobsites. The attached screenshot is from our current web portal dashboard . It shows how much material has been delivered from an order.

Dump trucks will deliver multiple loads during the day and the dispatcher uses the dashboard to monitor if they need to add more trucks or less trucks to fulfill the order. An example would be, I need to ship 1,000 tons of sand to a jobsite and I plan to use 10 trucks during the day and that it will take 10 hours of hauling to complete the job. After 5 hours of hauling (50% the day is over), I should have delivered 500 tons of sand (50% of the order). But maybe there is a lot of traffic, and I only have delivered 300 tons. The dashboard will show that I am behind schedule and I might need to add 2 more trucks to the job.

Industry/Entity Type

Construction

Font styles to use
Sans Serif

Requirements
Must have
• We need a progress bar showing how much material has been delivered, how much material was requested to be delivered total and how much material should have been delivered at the current time. The goal is to show the user if the deliveries are ahead or behind the expected pace and why.
Nice to have
• The icons for plant, driving and jobsite show if the actual times have exceeded or beaten the planned times. Maybe you have other ideas to show the user if the trucks are sitting longer on the jobsite, at the plant to get loaded or driving to and from the jobsite.

```html
<!DOCTYPE html>
<html lang="en">
<head>
<meta charset="utf-8">
<title>Delivery Performance Dashboard</title>
<link href="https://fonts.googleapis.com/css2?family=Poppins:wght@400;500&display=swap" rel="stylesheet">
<style>
:root{
  --bg:#eef4fd;
  --panel:#ffffff;
  --head-from:#6b6bd3;
  --head-to:#4a90e6;
  --table-head:#5a80dc;
  --text:#333842;
  --muted:#7a7f88;
  --rule:#e3e7ee;
  --ok:#28a745;
  --bad:#e53935;
  --blue:#0d6efd;
  --yellow:#ffc107;
  --green:#28a745;
  --teal:#17a2b8;
  --red:#dc3545;
  --icon:#7d8088;
}
*{box-sizing:border-box;margin:0;padding:0}
html,body{width:1200px;height:637px;overflow:hidden}
body{background:var(--bg);font-family:'Poppins',sans-serif;color:var(--text);position:relative}
.topbar{height:40px;background:linear-gradient(90deg,var(--head-from),var(--head-to));display:flex;align-items:center;padding:0 18px;color:#fff}
.brand{font-size:17px;font-weight:500}
.topbar-tools{margin-left:auto;display:flex;align-items:center;gap:0}
.search{width:160px;height:25px;background:#fff;border-radius:3px;display:flex;align-items:center;padding:0 8px;gap:6px;color:#b7bcc5;font-size:9px;margin-right:16px}
.tool{width:20px;height:20px;display:flex;align-items:center;justify-content:center;margin-right:16px;position:relative}
.badge{position:absolute;top:-3px;right:-4px;width:10px;height:10px;border-radius:50%;background:#f0506e;font-size:7px;display:flex;align-items:center;justify-content:center}
.avatar{width:32px;height:32px;border-radius:50%;background:linear-gradient(135deg,#c98a5c,#6b4a35);border:2px solid #fff;margin-right:14px}
.slogan{position:absolute;left:25px;top:68px;font-size:19px;font-weight:500;color:#3a3d44}
.orders{position:absolute;left:19px;top:117px;width:1174px;height:332px;background:var(--panel)}
.orders-head,.order-row{display:grid;grid-template-columns:73px 156px 161px 204px 76px 212px 121px 97px 1fr;align-items:center;padding-left:10px}
.orders-head{height:50px;background:var(--table-head);color:#fff;font-size:10.5px;padding-left:10px}
.orders-head span{display:flex;align-items:center;gap:8px}
.order-row{height:62px;border-bottom:1px solid var(--rule);font-size:10px;padding-left:23px}
.order-row:last-child{border-bottom:none}
.tons{padding-right:14px}
.tons-bar{height:6px;border-radius:3px;background:linear-gradient(90deg,#7c6fd4,#4d82e2);margin-bottom:8px;width:187px}
.tons-meta{display:flex;justify-content:space-between;width:187px;font-size:9px}
.waits{display:flex;align-items:center;gap:10px}
.wait{display:flex;align-items:center;gap:2px}
.ahead{color:var(--ok)}
.behind{color:var(--bad)}
.cards{position:absolute;top:462px;left:19px;display:flex;gap:7px}
.card{width:288px;height:150px;background:var(--panel);position:relative;padding:12px 0 0 15px}
.card-close{position:absolute;right:16px;top:10px;font-size:11px;color:#555}
.card-title{font-size:13.5px;color:#3a3d44}
.card-sub{font-size:9px;color:var(--muted);margin-top:3px}
.card-metric{display:flex;align-items:center;gap:6px;margin-top:14px;font-size:11px;color:#5d6068}
.meter{display:flex;align-items:center;margin-top:8px;font-size:10px;color:#6d7078;margin-left:-4px}
.meter-label{width:49px;text-align:right;margin-right:7px}
.meter-bar{height:7px;border-radius:4px}
.meter-value{margin-left:16px}
</style>
</head>
<body>
<header class="topbar">
  <div class="brand">Your Logo</div>
  <div class="topbar-tools">
    <div class="search">
      <svg width="11" height="11" viewBox="0 0 12 12"><circle cx="5" cy="5" r="3.5" fill="none" stroke="#666" stroke-width="1.4"/><path d="M7.6 7.6L11 11" stroke="#666" stroke-width="1.6"/></svg>
      Search...
    </div>
    <div class="tool"><svg width="16" height="15" viewBox="0 0 16 15"><path d="M1 1h14v9H6l-3 3v-3H1z" fill="none" stroke="#fff" stroke-width="1.5"/><path d="M4 4.5h8M4 7h6" stroke="#fff" stroke-width="1.2"/></svg></div>
    <div class="tool"><svg width="15" height="16" viewBox="0 0 15 16"><path d="M3 11V7a4.5 4.5 0 019 0v4l1.5 1.5h-12z" fill="none" stroke="#fff" stroke-width="1.5"/><path d="M6 14a1.5 1.5 0 003 0" stroke="#fff" stroke-width="1.3" fill="none"/></svg><span class="badge">2</span></div>
    <div class="avatar" role="img" aria-label="User profile photo"></div>
    <svg width="14" height="12" viewBox="0 0 14 12"><path d="M1 1h12M4 4.3h9M1 7.6h12M4 11h9" stroke="#fff" stroke-width="1.5"/></svg>
  </div>
</header>

<h1 class="slogan">Header Slogan Goes Here</h1>

<section class="orders">
  <div class="orders-head">
    <span>Order <svg width="6" height="18" viewBox="0 0 6 18"><path d="M1 5l2-2 2 2M1 13l2 2 2-2" stroke="#fff" stroke-width="1.2" fill="none"/></svg></span>
    <span>Origin <svg width="6" height="18" viewBox="0 0 6 18"><path d="M1 5l2-2 2 2M1 13l2 2 2-2" stroke="#fff" stroke-width="1.2" fill="none"/></svg></span>
    <span>Destination <svg width="6" height="18" viewBox="0 0 6 18"><path d="M1 5l2-2 2 2M1 13l2 2 2-2" stroke="#fff" stroke-width="1.2" fill="none"/></svg></span>
    <span>Customer <svg width="6" height="18" viewBox="0 0 6 18"><path d="M1 5l2-2 2 2M1 13l2 2 2-2" stroke="#fff" stroke-width="1.2" fill="none"/></svg></span>
    <span>Status <svg width="6" height="18" viewBox="0 0 6 18"><path d="M1 5l2-2 2 2M1 13l2 2 2-2" stroke="#fff" stroke-width="1.2" fill="none"/></svg></span>
    <span>Tons <svg style="margin-left:36px" width="6" height="18" viewBox="0 0 6 18"><path d="M1 5l2-2 2 2M1 13l2 2 2-2" stroke="#fff" stroke-width="1.2" fill="none"/></svg></span>
    <span>Wait Times <svg width="6" height="18" viewBox="0 0 6 18"><path d="M1 5l2-2 2 2M1 13l2 2 2-2" stroke="#fff" stroke-width="1.2" fill="none"/></svg></span>
    <span>Remaining <svg width="6" height="18" viewBox="0 0 6 18"><path d="M1 5l2-2 2 2M1 13l2 2 2-2" stroke="#fff" stroke-width="1.2" fill="none"/></svg></span>
    <span>+/- <svg width="12" height="9" viewBox="0 0 12 9"><path d="M0 1h7v5H0zM7 3h3l2 2v1H7z" fill="#fff"/><circle cx="2.5" cy="7.3" r="1.4" fill="#fff"/><circle cx="9.5" cy="7.3" r="1.4" fill="#fff"/></svg></span>
  </div>

  <div class="order-row">
    <span>177746</span><span>Ashford Asphalt Plant</span><span>BZJV-185 from mm 77-98</span><span>Harlow Construction - North Division</span><span>Accepted</span>
    <div class="tons"><div class="tons-bar"></div><div class="tons-meta"><span>722.57 / 1500</span><span>7:30 am - 5:00 pm</span></div></div>
    <div class="waits">
      <span class="wait"><svg width="11" height="9" viewBox="0 0 11 9"><path d="M0 9V1h2v4l3-2v2l3-2v6z" fill="var(--icon)"/></svg><svg width="6" height="4" viewBox="0 0 6 4"><path d="M0 4l3-4 3 4z" fill="var(--bad)"/></svg></span>
      <span class="wait"><svg width="12" height="9" viewBox="0 0 12 9"><path d="M0 1h7v5H0zM7 3h3l2 2v1H7z" fill="var(--icon)"/><circle cx="2.5" cy="7.3" r="1.4" fill="var(--icon)"/><circle cx="9.5" cy="7.3" r="1.4" fill="var(--icon)"/></svg><svg width="6" height="4" viewBox="0 0 6 4"><path d="M0 4l3-4 3 4z" fill="var(--bad)"/></svg></span>
      <span class="wait"><svg width="8" height="10" viewBox="0 0 8 10"><path d="M4 10L1 5.5a3.5 3.5 0 116 0z" fill="var(--icon)"/><circle cx="4" cy="3.6" r="1.3" fill="#fff"/></svg><svg width="6" height="4" viewBox="0 0 6 4"><path d="M0 0l3 4 3-4z" fill="var(--ok)"/></svg></span>
    </div>
    <span class="ahead">+1:25 hrs</span><span class="behind">-31</span>
  </div>

  <div class="order-row">
    <span>177746</span><span>Ashford Asphalt Plant</span><span>BZJV-185 from mm 77-98</span><span>Harlow Construction - North Division</span><span>Accepted</span>
    <div class="tons"><div class="tons-bar"></div><div class="tons-meta"><span>722.57 / 1500</span><span>7:30 am - 5:00 pm</span></div></div>
    <div class="waits">
      <span class="wait"><svg width="11" height="9" viewBox="0 0 11 9"><path d="M0 9V1h2v4l3-2v2l3-2v6z" fill="var(--icon)"/></svg><svg width="6" height="4" viewBox="0 0 6 4"><path d="M0 4l3-4 3 4z" fill="var(--bad)"/></svg></span>
      <span class="wait"><svg width="12" height="9" viewBox="0 0 12 9"><path d="M0 1h7v5H0zM7 3h3l2 2v1H7z" fill="var(--icon)"/><circle cx="2.5" cy="7.3" r="1.4" fill="var(--icon)"/><circle cx="9.5" cy="7.3" r="1.4" fill="var(--icon)"/></svg><svg width="6" height="4" viewBox="0 0 6 4"><path d="M0 4l3-4 3 4z" fill="var(--bad)"/></svg></span>
      <span class="wait"><svg width="8" height="10" viewBox="0 0 8 10"><path d="M4 10L1 5.5a3.5 3.5 0 116 0z" fill="var(--icon)"/><circle cx="4" cy="3.6" r="1.3" fill="#fff"/></svg><svg width="6" height="4" viewBox="0 0 6 4"><path d="M0 0l3 4 3-4z" fill="var(--ok)"/></svg></span>
    </div>
    <span class="ahead">+1:25 hrs</span><span class="behind">-31</span>
  </div>

  <div class="order-row">
    <span>177746</span><span>Ashford Asphalt Plant</span><span>BZJV-185 from mm 77-98</span><span>Harlow Construction - North Division</span><span>Accepted</span>
    <div class="tons"><div class="tons-bar"></div><div class="tons-meta"><span>722.57 / 1500</span><span>7:30 am - 5:00 pm</span></div></div>
    <div class="waits">
      <span class="wait"><svg width="11" height="9" viewBox="0 0 11 9"><path d="M0 9V1h2v4l3-2v2l3-2v6z" fill="var(--icon)"/></svg><svg width="6" height="4" viewBox="0 0 6 4"><path d="M0 4l3-4 3 4z" fill="var(--bad)"/></svg></span>
      <span class="wait"><svg width="12" height="9" viewBox="0 0 12 9"><path d="M0 1h7v5H0zM7 3h3l2 2v1H7z" fill="var(--icon)"/><circle cx="2.5" cy="7.3" r="1.4" fill="var(--icon)"/><circle cx="9.5" cy="7.3" r="1.4" fill="var(--icon)"/></svg><svg width="6" height="4" viewBox="0 0 6 4"><path d="M0 4l3-4 3 4z" fill="var(--bad)"/></svg></span>
      <span class="wait"><svg width="8" height="10" viewBox="0 0 8 10"><path d="M4 10L1 5.5a3.5 3.5 0 116 0z" fill="var(--icon)"/><circle cx="4" cy="3.6" r="1.3" fill="#fff"/></svg><svg width="6" height="4" viewBox="0 0 6 4"><path d="M0 0l3 4 3-4z" fill="var(--ok)"/></svg></span>
    </div>
    <span class="ahead">+1:25 hrs</span><span class="behind">-31</span>
  </div>

  <div class="order-row">
    <span>177746</span><span>Ashford Asphalt Plant</span><span>BZJV-185 from mm 77-98</span><span>Harlow Construction - North Division</span><span>Accepted</span>
    <div class="tons"><div class="tons-bar"></div><div class="tons-meta"><span>722.57 / 1500</span><span>7:30 am - 5:00 pm</span></div></div>
    <div class="waits">
      <span class="wait"><svg width="11" height="9" viewBox="0 0 11 9"><path d="M0 9V1h2v4l3-2v2l3-2v6z" fill="var(--icon)"/></svg><svg width="6" height="4" viewBox="0 0 6 4"><path d="M0 4l3-4 3 4z" fill="var(--bad)"/></svg></span>
      <span class="wait"><svg width="12" height="9" viewBox="0 0 12 9"><path d="M0 1h7v5H0zM7 3h3l2 2v1H7z" fill="var(--icon)"/><circle cx="2.5" cy="7.3" r="1.4" fill="var(--icon)"/><circle cx="9.5" cy="7.3" r="1.4" fill="var(--icon)"/></svg><svg width="6" height="4" viewBox="0 0 6 4"><path d="M0 4l3-4 3 4z" fill="var(--bad)"/></svg></span>
      <span class="wait"><svg width="8" height="10" viewBox="0 0 8 10"><path d="M4 10L1 5.5a3.5 3.5 0 116 0z" fill="var(--icon)"/><circle cx="4" cy="3.6" r="1.3" fill="#fff"/></svg><svg width="6" height="4" viewBox="0 0 6 4"><path d="M0 0l3 4 3-4z" fill="var(--ok)"/></svg></span>
    </div>
    <span class="ahead">+1:25 hrs</span><span class="behind">-31</span>
  </div>
</section>

<section class="cards">
  <article class="card">
    <span class="card-close">✕</span>
    <h2 class="card-title">Order 17746</h2>
    <p class="card-sub">Avg Cycle Time : 2 hrs 27 min</p>
    <div class="card-metric"><svg width="18" height="15" viewBox="0 0 11 9"><path d="M0 9V1h2v4l3-2v2l3-2v6z" fill="var(--icon)"/></svg>Plant (min)</div>
    <div class="meter"><span class="meter-label">Planned</span><span class="meter-bar" style="width:140px;background:var(--blue)"></span><span class="meter-value" style="margin-left:20px">30</span></div>
    <div class="meter"><span class="meter-label">Actual</span><span class="meter-bar" style="width:173px;background:var(--red)"></span><span class="meter-value">33</span></div>
  </article>
  <article class="card">
    <span class="card-close">✕</span>
    <h2 class="card-title">Order 17746</h2>
    <p class="card-sub">Avg Cycle Time : 2 hrs 27 min</p>
    <div class="card-metric"><svg width="22" height="17" viewBox="0 0 12 9"><path d="M0 1h7v5H0zM7 3h3l2 2v1H7z" fill="var(--icon)"/><circle cx="2.5" cy="7.3" r="1.4" fill="var(--icon)"/><circle cx="9.5" cy="7.3" r="1.4" fill="var(--icon)"/></svg>Diving (min)</div>
    <div class="meter"><span class="meter-label">Planned</span><span class="meter-bar" style="width:104px;background:var(--yellow)"></span><span class="meter-value" style="margin-left:10px">60</span></div>
    <div class="meter"><span class="meter-label">Actual</span><span class="meter-bar" style="width:197px;background:var(--red)"></span><span class="meter-value" style="margin-left:9px">83</span></div>
  </article>
  <article class="card">
    <span class="card-close">✕</span>
    <h2 class="card-title">Order 17746</h2>
    <p class="card-sub">Avg Cycle Time : 2 hrs 27 min</p>
    <div class="card-metric"><svg width="14" height="18" viewBox="0 0 8 10"><path d="M4 10L1 5.5a3.5 3.5 0 116 0z" fill="var(--icon)"/><circle cx="4" cy="3.6" r="1.3" fill="#fff"/></svg>Jobsite (min)</div>
    <div class="meter"><span class="meter-label">Planned</span><span class="meter-bar" style="width:140px;background:var(--green)"></span><span class="meter-value" style="margin-left:10px">30</span></div>
    <div class="meter"><span class="meter-label">Actual</span><span class="meter-bar" style="width:140px;background:var(--green)"></span><span class="meter-value" style="margin-left:10px">30</span></div>
  </article>
  <article class="card">
    <span class="card-close">✕</span>
    <h2 class="card-title">Order 17746</h2>
    <p class="card-sub">Avg Cycle Time : 2 hrs 27 min</p>
    <div class="card-metric"><svg width="17" height="17" viewBox="0 0 16 16"><path d="M8 0l1.5 2.3 2.6-.9.3 2.7 2.7.3-.9 2.6L16 8l-2.3 1.5.9 2.6-2.7.3-.3 2.7-2.6-.9L8 16l-1.5-2.3-2.6.9-.3-2.7-2.7-.3.9-2.6L0 8l2.3-1.5-.9-2.6 2.7-.3.3-2.7 2.6.9z" fill="var(--icon)"/><circle cx="8" cy="8" r="2.6" fill="#fff"/></svg>Equipment (min)</div>
    <div class="meter"><span class="meter-label">Planned</span><span class="meter-bar" style="width:104px;background:var(--teal)"></span><span class="meter-value" style="margin-left:8px">60</span></div>
    <div class="meter"><span class="meter-label">Actual</span><span class="meter-bar" style="width:181px;background:var(--red)"></span><span class="meter-value" style="margin-left:5px">83</span></div>
  </article>
</section>
</body>
</html>
```